Professional, Scientific Cover Design for Nutritional / Hair Tissue Mineral Analysis (HTMA) Company

Hair tissue mineral analysis is a versatile, science-backed tool that offers a deeper understanding of your body's mineral and heavy metal profile. By evaluating long-term mineral balance and toxic exposures, HTMA provides invaluable insights that can aid in optimizing nutrition, addressing chronic health issues, and creating a personalized wellness strategy.

We have updated our logo and are in need of an updated report cover in which personalized test results are placed. We are looking for a professional and more modern look.

There are 2 small cutouts that will need to remain as shown in the picture in the brief.

Our updated logo along with color palette used will be uploaded in the brief as well as our 2 previous, outdated designs. We no longer want our address on the front cover. We also do not want images with people in them.

Thank you.

Website: www.pevdosk.com

Designs look the same

• Images with people

```html
<!DOCTYPE html>
<html lang="en">
<head>
<meta charset="utf-8">
<title>Tissue Mineral Analysis – Report Cover</title>
<link href="https://fonts.googleapis.com/css2?family=Titillium+Web:wght@300;400;700&display=swap" rel="stylesheet">
<style>
  :root{
    --stage:#1a1d36;
    --paper:#ffffff;
    --brand-blue:#2e5a9e;
    --brand-orange:#ef8229;
    --fold:#f3f3f3;
    --cutout-line:#c9c9c9;
  }
  *{box-sizing:border-box;margin:0;padding:0}
  html,body{width:1200px;height:1200px;overflow:hidden;background:var(--stage)}
  body{position:relative;font-family:"Titillium Web",sans-serif}
  .spread{position:absolute;left:41px;top:205px;width:1117px;height:789px;background:var(--paper);overflow:hidden}
  .spread-art{position:absolute;inset:0;width:100%;height:100%}
  .brand-name{position:absolute;color:var(--brand-blue);font-weight:700;text-transform:uppercase;white-space:nowrap;display:flex;align-items:center}
  .brand-name .dot{display:inline-block;border-radius:50%;background:var(--brand-blue)}
  .brand-back{left:94px;top:108px;font-size:31px;letter-spacing:.08em}
  .brand-back .dot{width:16px;height:16px;margin-right:10px}
  .brand-front{left:872px;top:692px;font-size:15px;letter-spacing:.08em}
  .brand-front .dot{width:9px;height:9px;margin-right:7px}
  .website{position:absolute;left:94px;top:712px;font-size:14px;font-weight:400;letter-spacing:.55em;color:var(--brand-blue);text-transform:uppercase}
  .title{position:absolute;left:559px;width:558px;text-align:center;color:var(--brand-blue);text-transform:uppercase}
  .title-main{top:175px;font-size:25px;font-weight:700;letter-spacing:.62em;padding-left:.62em}
  .title-sub{top:210px;font-size:25px;font-weight:300;letter-spacing:.62em;padding-left:.62em}
  .cutout{position:absolute;top:280px;width:213px;height:27px;border:1px solid var(--cutout-line);border-radius:6px}
  .cutout-left{left:616px}
  .cutout-right{left:848px}
</style>
</head>
<body>
  <main class="spread">
    <svg class="spread-art" viewBox="66 330 1799 1271" preserveAspectRatio="none">
      <defs>
        <linearGradient id="band-tone" x1="0" x2="1" y1="0" y2="1">
          <stop offset="0" stop-color="var(--brand-blue)"/>
          <stop offset="0.65" stop-color="var(--brand-blue)"/>
          <stop offset="1" stop-color="var(--brand-orange)"/>
        </linearGradient>
        <linearGradient id="fold-tint" x1="0" x2="1" y1="0" y2="0">
          <stop offset="0" stop-color="#f3f3f3" stop-opacity="0"/>
          <stop offset="0.4" stop-color="#f3f3f3"/>
          <stop offset="1" stop-color="#f3f3f3"/>
        </linearGradient>
        <linearGradient id="fold-shade" x1="0" x2="1" y1="0" y2="0">
          <stop offset="0" stop-color="#ffffff" stop-opacity="0"/>
          <stop offset="1" stop-color="#ffffff" stop-opacity="0.25"/>
        </linearGradient>
      </defs>
      <rect class="fold-tint" x="885" y="330" width="81" height="1271" fill="url(#fold-tint)" aria-hidden="true"/>
      <polygon class="corner-decoration" role="img" aria-label="Decorative blue and orange corner band"
        points="66,435 210,330 465,330 66,628" fill="url(#band-tone)"/>
      <polygon class="sweep-decoration" role="img" aria-label="Decorative blue and orange sweeping band"
        points="592,1601 1865,957 1865,1142 1255,1601" fill="url(#band-tone)"/>
      <rect class="fold-highlight" x="885" y="1280" width="81" height="321" fill="url(#fold-shade)" aria-hidden="true"/>
    </svg>

    <div class="brand-name brand-back"><span class="dot"></span>Pevdosk</div>
    <p class="website">www.pevdosk.com</p>

    <h1 class="title title-main">Tissue Mineral</h1>
    <p class="title title-sub">Analysis</p>

    <div class="cutout cutout-left"></div>
    <div class="cutout cutout-right"></div>

    <div class="brand-name brand-front"><span class="dot"></span>Pevdosk Research Labs</div>
  </main>
</body>
</html>
```